Bref créative
Blue Maple Holdings, LLC
Business cards, stationary and envelopes, electronic stationary (Microsoft Word), email signature
Simple
Peter L. Ward
Managing Member
5180 Halvern Court, Suite 4
Larkton, OH 45999
pward@bmholdco.example
Phone, email, and name will change for the additional members of the company.
We also want an electronic email signature, and electronic stationary to be used with Microsoft word.
Stationary and envelopes should tie in the theme of the business cards for a uniform look.
Also looking for a Header only version of the stationary, as well as a full page version (header and footer used for design).
Logo used in a creative way.
Horizontal Black Background
Horizontal ALL Black
Horizontal White Background
Horizontal ALL White
Vertical Black Background
Vertical ALL Black
Vertical White Background
Vertical ALL White

```html
<!DOCTYPE html>
<html lang="en">
<head>
<meta charset="utf-8">
<title>Blue Maple Holdings – Business Cards</title>
<link href="https://fonts.googleapis.com/css2?family=Open+Sans:wght@400;600;700&display=swap" rel="stylesheet">
<style>
  :root {
    --bg: #ece9e6;
    --card: #ffffff;
    --red: #c4161c;
    --red-dark: #8e0f14;
    --navy: #1f3c7a;
    --grey: #4d4d4d;
    --rule: #cfcfcf;
  }
  * { margin: 0; padding: 0; box-sizing: border-box; }
  html, body { width: 1200px; height: 852px; overflow: hidden; }
  body {
    background: var(--bg);
    font-family: "Open Sans", Arial, sans-serif;
    color: var(--grey);
    position: relative;
  }
  .card {
    position: absolute;
    width: 640px;
    height: 366px;
    background: var(--card);
    border-radius: 18px;
    overflow: hidden;
    box-shadow: 0 6px 18px rgba(0,0,0,.18);
  }
  .card--vertical { left: 280px; top: 46px; }
  .card--horizontal { left: 280px; top: 440px; }
  .card__band { position: absolute; left: 0; bottom: 0; width: 640px; height: 110px; }

  .brand { font-weight: 700; color: var(--red); letter-spacing: 2px; text-transform: uppercase; line-height: 1.05; }
  .brand__mark { display: inline-block; width: 46px; height: 46px; background: var(--red); border-radius: 4px; }

  /* vertical card */
  .card--vertical .brand-block { position: absolute; left: 48px; top: 76px; width: 220px; text-align: center; }
  .card--vertical .brand-block .brand__mark { margin-bottom: 14px; }
  .card--vertical .brand { font-size: 25px; }
  .card--vertical .divider { position: absolute; left: 300px; top: 34px; width: 1px; height: 200px; background: var(--rule); }
  .card--vertical .details { position: absolute; left: 322px; top: 34px; }

  .person__name { font-size: 19px; font-weight: 700; color: var(--red); }
  .person__title { font-size: 14px; font-weight: 600; color: var(--navy); margin-bottom: 22px; }
  .address { font-size: 13px; line-height: 1.45; margin-bottom: 22px; }
  .contacts { list-style: none; font-size: 13px; line-height: 1.6; }
  .contacts li { display: flex; align-items: center; gap: 8px; }
  .contacts svg { width: 12px; height: 12px; fill: var(--red); flex: none; }

  /* horizontal card */
  .card--horizontal .brand-block { position: absolute; left: 130px; top: 46px; display: flex; align-items: center; gap: 16px; }
  .card--horizontal .brand { font-size: 30px; }
  .card--horizontal .rule { position: absolute; left: 40px; right: 40px; top: 128px; height: 1px; background: var(--rule); }
  .card--horizontal .person { position: absolute; left: 40px; top: 150px; width: 270px; text-align: right; }
  .card--horizontal .person__title { margin-bottom: 8px; }
  .card--horizontal .address { margin-bottom: 0; }
  .card--horizontal .divider { position: absolute; left: 330px; top: 146px; width: 1px; height: 96px; background: var(--rule); }
  .card--horizontal .contacts { position: absolute; left: 350px; top: 146px; }
</style>
</head>
<body>

<article class="card card--vertical">
  <div class="brand-block">
    <span class="brand__mark"></span>
    <div class="brand">Blue Maple<br>Holdings</div>
  </div>
  <div class="divider"></div>
  <div class="details">
    <div class="person__name">Peter L. Ward</div>
    <div class="person__title">Managing Member</div>
    <div class="address">5180 Halvern Court,<br>Suite 4, Larkton,<br>OH 45999</div>
    <ul class="contacts">
      <li><svg viewBox="0 0 12 12"><path d="M2 0h3l1 3-2 1.5a7 7 0 0 0 3.5 3.5L9 6l3 1v3a2 2 0 0 1-2 2C4.5 12 0 7.5 0 2a2 2 0 0 1 2-2z"/></svg>(555) 014-2280</li>
      <li><svg viewBox="0 0 12 12"><rect x="3" y="0" width="6" height="12" rx="1.5"/></svg>(555) 018-3361</li>
      <li><svg viewBox="0 0 12 12"><rect x="1" y="3" width="10" height="8" rx="1"/><rect x="3" y="0" width="6" height="3"/></svg>(555) 019-4472</li>
      <li><svg viewBox="0 0 12 12"><path d="M0 2h12v8H0z M0 2l6 5 6-5"/></svg>pward@bmholdco.example</li>
    </ul>
  </div>
  <svg class="card__band" viewBox="0 0 640 110" preserveAspectRatio="none">
    <path d="M0 30 Q320 72 640 44 L640 56 Q320 84 0 44 Z" fill="var(--grey)"/>
    <path d="M0 52 Q320 92 640 62 L640 110 L0 110 Z" fill="var(--red)"/>
    <path d="M0 90 Q320 104 640 88 L640 110 L0 110 Z" fill="var(--red-dark)" opacity=".5"/>
  </svg>
</article>

<article class="card card--horizontal">
  <div class="brand-block">
    <span class="brand__mark"></span>
    <div class="brand">Blue Maple Holdings</div>
  </div>
  <div class="rule"></div>
  <div class="person">
    <div class="person__name">Peter L. Ward</div>
    <div class="person__title">Managing Member</div>
    <div class="address">5180 Halvern Court, Suite 4<br>Larkton, OH 45999</div>
  </div>
  <div class="divider"></div>
  <ul class="contacts">
    <li><svg viewBox="0 0 12 12"><path d="M2 0h3l1 3-2 1.5a7 7 0 0 0 3.5 3.5L9 6l3 1v3a2 2 0 0 1-2 2C4.5 12 0 7.5 0 2a2 2 0 0 1 2-2z"/></svg>(555) 014-2280</li>
    <li><svg viewBox="0 0 12 12"><rect x="3" y="0" width="6" height="12" rx="1.5"/></svg>(555) 018-3361</li>
    <li><svg viewBox="0 0 12 12"><rect x="1" y="3" width="10" height="8" rx="1"/><rect x="3" y="0" width="6" height="3"/></svg>(555) 019-4472</li>
    <li><svg viewBox="0 0 12 12"><path d="M0 2h12v8H0z M0 2l6 5 6-5"/></svg>pward@bmholdco.example</li>
  </ul>
  <svg class="card__band" viewBox="0 0 640 110" preserveAspectRatio="none">
    <path d="M0 44 Q320 80 640 36 L640 48 Q320 92 0 56 Z" fill="var(--grey)"/>
    <path d="M0 64 Q320 100 640 56 L640 110 L0 110 Z" fill="var(--red)"/>
    <path d="M0 94 Q320 106 640 86 L640 110 L0 110 Z" fill="var(--red-dark)" opacity=".5"/>
  </svg>
</article>

</body>
</html>
```